KOVER Wealth Partners Brochure
Brochure Design 2011
Your Objectives Through Independence
We need a tri-fold brochure for our company KOVER Wealth Partners. We already have a custom logo created and need that inserted into the brochure. We are a independent financial services company, we offer investment advice and products to consumers and business.
Financial Services
Consumers & Business
Must use our current company logo,you can get it here:
https://photoshelf-example.net/MarcusLindt/KOVERWealthPartners?authkey=Xq7TmLbNZr2Wd9YkHfPe&feat=directlink
Also need all content including sections to be editable. Need at least three sections (Example: "The Company", "Our Services", etc...)
KOVER Wealth Partners Logo
Logo AI file
Logo AI File 2.0
Old Brochure Cover (Prime Ledger)
old brochure Inner (Prime Ledger)
This is a brochure which I like the style, simple and clean
Another Brochure in which I like
by far my favorite one, hope this inspires some ideas
more ideas

```html
<!DOCTYPE html>
<html lang="en">
<head>
<meta charset="utf-8">
<title>KOVER Wealth Partners Brochure</title>
<link rel="stylesheet" href="https://fonts.googleapis.com/css2?family=Oswald:wght@300;400&family=Open+Sans:ital,wght@0,400;0,600;0,700;1,400;1,700&display=swap">
<style>
  :root {
    --canvas: #e8e8e4;
    --paper: #ffffff;
    --charcoal: #43484e;
    --charcoal-dark: #33373c;
    --lime: #c6d300;
    --cyan: #1fa9d6;
    --magenta: #d6246e;
    --green: #8cc63f;
    --orange: #f39a1e;
    --ink: #4b4f54;
    --muted: #8a8e93;
  }
  * { box-sizing: border-box; margin: 0; padding: 0; }
  html, body { width: 1200px; height: 667px; overflow: hidden; }
  body { background: var(--canvas); font-family: "Open Sans", Arial, sans-serif; color: var(--ink); position: relative; }

  /* Inside spread */
  .inside-spread { position: absolute; left: 40px; top: 60px; width: 620px; height: 547px; background: var(--paper); display: flex; box-shadow: 0 2px 8px rgba(0,0,0,.15); }
  .section-rail { width: 64px; display: flex; flex-direction: column; }
  .rail-label { flex: 1; display: flex; align-items: center; justify-content: center; }
  .rail-label span { transform: rotate(-90deg); font-family: "Oswald", sans-serif; font-size: 30px; font-weight: 300; color: #fff; white-space: nowrap; letter-spacing: 1px; }
  .rail-about { background: var(--charcoal); flex: 0 0 200px; }
  .rail-services { background: var(--lime); }
  .rail-services span { color: var(--charcoal); }
  .spread-body { flex: 1; padding: 24px 26px; display: flex; flex-direction: column; gap: 20px; }
  .about-block { display: flex; gap: 20px; height: 156px; border-bottom: 2px solid var(--lime); padding-bottom: 18px; }
  .about-text { flex: 1; font-size: 13px; line-height: 1.6; }
  .about-text .lead { font-size: 15px; font-weight: 600; color: var(--charcoal); margin-bottom: 8px; }
  .about-visual { width: 190px; border-radius: 2px; background: linear-gradient(135deg, #f4f4f4, #c9cbce); }
  .services-grid { flex: 1; display: grid; grid-template-columns: 1fr 1fr; gap: 18px 22px; }
  .service { display: flex; flex-direction: column; gap: 6px; }
  .service-head { display: flex; align-items: center; gap: 10px; }
  .service-visual { width: 58px; height: 44px; border-radius: 2px; }
  .service-title { font-family: "Oswald", sans-serif; font-size: 20px; font-weight: 400; }
  .service p { font-size: 12px; line-height: 1.5; }
  .investment .service-title { color: var(--cyan); } .investment .service-visual { background: linear-gradient(135deg, #bfe6f4, var(--cyan)); }
  .real-estate .service-title { color: var(--magenta); } .real-estate .service-visual { background: linear-gradient(135deg, #f3c0d4, var(--magenta)); }
  .retirement .service-title { color: var(--green); } .retirement .service-visual { background: linear-gradient(135deg, #dcefc4, var(--green)); }
  .banking .service-title { color: var(--orange); } .banking .service-visual { background: linear-gradient(135deg, #fbdcae, var(--orange)); }

  /* Cover */
  .cover { position: absolute; left: 700px; top: 60px; width: 460px; height: 547px; background: var(--paper); box-shadow: 0 2px 8px rgba(0,0,0,.15); display: flex; flex-direction: column; }
  .tab-row { height: 54px; display: flex; gap: 6px; padding: 12px 18px 0; }
  .tab { flex: 1; border-top: 10px solid; font-size: 9px; padding-top: 4px; color: var(--muted); text-transform: lowercase; }
  .tab.investment { border-color: var(--cyan); } .tab.real-estate { border-color: var(--magenta); }
  .tab.retirement { border-color: var(--green); } .tab.insurance { border-color: var(--charcoal); } .tab.planning { border-color: var(--orange); }
  .cover-hero { position: relative; height: 300px; background: linear-gradient(160deg, var(--charcoal), var(--charcoal-dark)); overflow: hidden; }
  .cover-headline { position: absolute; left: 40px; top: 56px; font-family: "Oswald", sans-serif; font-weight: 300; text-transform: uppercase; line-height: 1.05; color: #fff; }
  .cover-headline .line { display: block; font-size: 36px; }
  .cover-headline .accent { color: var(--lime); }
  .brand { position: absolute; right: 24px; top: 50px; display: flex; align-items: center; gap: 8px; font-family: "Open Sans", sans-serif; font-weight: 600; font-size: 13px; color: #fff; width: 120px; line-height: 1.2; }
  .brand-mark { width: 22px; height: 22px; background: #fff; flex: 0 0 22px; }
  .hero-photo { position: absolute; left: 0; bottom: 0; width: 230px; height: 110px; background: linear-gradient(90deg, rgba(0,0,0,.35), rgba(90,96,102,.4)); }
  .quote-band { background: var(--lime); padding: 22px 30px; display: flex; gap: 12px; }
  .quote-mark { font-family: "Oswald", sans-serif; font-size: 48px; line-height: .8; color: var(--charcoal); }
  .quote-band p { font-style: italic; font-size: 14px; line-height: 1.5; color: var(--charcoal); }
  .quote-band strong { font-weight: 700; }
  .cover-foot { flex: 1; }
</style>
</head>
<body>
  <section class="inside-spread">
    <div class="section-rail">
      <div class="rail-label rail-about"><span>about us</span></div>
      <div class="rail-label rail-services"><span>services</span></div>
    </div>
    <div class="spread-body">
      <div class="about-block">
        <div class="about-text">
          <p class="lead">Founded on independent advice, we help clients align financial choices with lasting personal goals.</p>
          <p>Every plan starts with listening.</p>
        </div>
        <div class="about-visual" role="img" aria-label="Grey three-dimensional figures illustration"></div>
      </div>
      <div class="services-grid">
        <div class="service investment">
          <div class="service-head"><div class="service-visual" role="img" aria-label="Investment illustration"></div><h3 class="service-title">investment</h3></div>
          <p>Portfolios built around your risk, timeline and objectives.</p>
        </div>
        <div class="service real-estate">
          <div class="service-head"><div class="service-visual" role="img" aria-label="Houses illustration"></div><h3 class="service-title">real estate</h3></div>
          <p>Our real estate agents work closely with buyers and sellers.</p>
        </div>
        <div class="service retirement">
          <div class="service-head"><div class="service-visual" role="img" aria-label="Retirement illustration"></div><h3 class="service-title">retirement</h3></div>
          <p>We provide estate planning and preparation for every stage.</p>
        </div>
        <div class="service banking">
          <div class="service-head"><div class="service-visual" role="img" aria-label="Bank building illustration"></div><h3 class="service-title">banking</h3></div>
          <p>KOVER has become the trusted partner for local businesses.</p>
        </div>
      </div>
    </div>
  </section>

  <section class="cover">
    <div class="tab-row">
      <div class="tab investment">investment</div>
      <div class="tab real-estate">real estate</div>
      <div class="tab retirement">retirement</div>
      <div class="tab insurance">insurance</div>
      <div class="tab planning">planning</div>
    </div>
    <div class="cover-hero">
      <h1 class="cover-headline">
        <span class="line accent">Your Objectives</span>
        <span class="line">Through</span>
        <span class="line accent">Independence</span>
      </h1>
      <div class="brand"><span class="brand-mark"></span><span>KOVER Wealth Partners</span></div>
      <div class="hero-photo" role="img" aria-label="Photo of a hand at a laptop keyboard"></div>
    </div>
    <div class="quote-band">
      <span class="quote-mark">&ldquo;</span>
      <p>KOVER's single source financial services business model is <strong>brilliant</strong> in its simplicity and execution.</p>
    </div>
    <div class="cover-foot"></div>
  </section>
</body>
</html>
```